Event flyer for Sunday night Youth Group

Need a 4 x 6 or 5 x 7 flyer for a new youth group starting on April 14. The youth group is for students in middle school and high school so it needs to look fun and cool, but not childish. I prefer it not to include pictures of people unless it's so obscure you can't really see their faces. I've uploaded some pictures of flyers I like. I've also attached a couple versions of our logo to use on the flyer.
Information the flyer needs to include:
Youth Group
Sundays, 6-8pm (beginning April 14)
Location: Merriwick's - 4219 Hollowfern Ln S, Keizer, 97418
There will be dinner, games, friends, and a message.
Target Market(s)
Youth ages 13-18
Industry/Entity Type
Church
Colors
Designer to choose colors to be used in the design.
Look and feel

```html
<!DOCTYPE html>
<html lang="en">
<head>
<meta charset="utf-8">
<title>Youth Group Flyer</title>
<link rel="stylesheet" href="https://fonts.googleapis.com/css2?family=Luckiest+Guy&family=Montserrat:ital,wght@0,400;0,600;0,700;1,700&display=swap">
<style>
  :root {
    --page-bg: #dcdcdc;
    --flyer-top: #818f7c;
    --flyer-mid: #52686a;
    --flyer-bottom: #2b4551;
    --ink-navy: #24404f;
    --olive: #7f8b74;
    --white: #ffffff;
    --crowd-light: rgba(70, 92, 94, 0.55);
    --crowd-dark: rgba(36, 58, 68, 0.55);
  }
  * { margin: 0; padding: 0; box-sizing: border-box; }
  html, body { width: 1200px; height: 1200px; overflow: hidden; }
  body { background: var(--page-bg); position: relative; font-family: "Montserrat", sans-serif; }

  .flyer {
    position: absolute;
    left: 239px; top: 57px;
    width: 722px; height: 1084px;
    overflow: hidden;
    background: linear-gradient(to bottom, var(--flyer-top) 0%, var(--flyer-mid) 55%, var(--flyer-bottom) 88%, var(--flyer-bottom) 100%);
    box-shadow: 0 2px 6px rgba(0,0,0,0.18);
  }

  .brand {
    position: absolute;
    left: 0; right: 0; top: 150px;
    display: flex; align-items: center; justify-content: center; gap: 18px;
    color: var(--white);
    font-weight: 600;
    font-size: 40px;
    letter-spacing: 0.5px;
  }
  .brand-mark { width: 34px; height: 34px; background: var(--white); }

  .torn-band { position: absolute; left: 0; top: 285px; width: 722px; height: 285px; }

  .crowd {
    position: absolute;
    left: 0; right: 0; top: 660px; height: 424px;
    background: linear-gradient(to bottom, rgba(0,0,0,0) 0%, var(--crowd-light) 25%, var(--crowd-dark) 60%, rgba(0,0,0,0) 100%);
  }

  .headline {
    position: absolute; left: 0; right: 0;
    text-align: center;
    font-family: "Luckiest Guy", sans-serif;
    line-height: 1;
  }
  .headline-youth {
    top: 360px;
    font-size: 158px;
    color: var(--ink-navy);
    letter-spacing: 2px;
    text-shadow: 4px 4px 0 rgba(0,0,0,0.12);
  }
  .headline-group {
    top: 500px;
    font-size: 156px;
    color: var(--white);
    letter-spacing: 2px;
    -webkit-text-stroke: 16px var(--olive);
    paint-order: stroke fill;
  }

  .details { position: absolute; left: 0; right: 0; text-align: center; color: var(--white); }
  .schedule { top: 735px; font-size: 35px; font-weight: 600; }
  .start-date { top: 780px; font-size: 27px; font-weight: 400; opacity: 0.92; }

  .location {
    position: absolute;
    left: 21px; top: 857px;
    width: 680px; height: 52px;
    background: var(--white);
    color: var(--ink-navy);
    font-size: 24px; font-weight: 600;
    display: flex; align-items: center; justify-content: center;
  }

  .tagline {
    top: 955px;
    font-size: 22px; font-weight: 700; font-style: italic;
    line-height: 30px;
  }
</style>
</head>
<body>
  <main class="flyer">
    <div class="brand"><span class="brand-mark"></span><span class="brand-name">Cedar Path Church</span></div>

    <svg class="torn-band" viewBox="0 0 722 285" aria-hidden="true">
      <polygon fill="#ffffff" points="0,40 28,22 55,34 84,8 110,30 140,18 168,38 196,12 230,28 258,6 290,30 318,16 350,36 380,10 410,26 440,14 470,34 500,8 530,24 560,12 590,32 620,6 650,26 680,14 704,30 722,0 722,150 700,170 672,158 640,182 612,166 580,188 548,170 516,192 486,176 452,198 420,180 388,204 356,186 322,206 290,188 258,210 226,190 194,212 162,194 130,214 98,196 66,216 34,198 0,214"/>
    </svg>

    <div class="crowd" role="img" aria-label="Faint silhouettes of a crowd with raised hands"></div>

    <h1 class="headline headline-youth">YOUTH</h1>
    <div class="headline headline-group">GROUP</div>

    <p class="details schedule">Sundays, 6-8pm</p>
    <p class="details start-date">(beginning April 14)</p>

    <div class="location">Merriwick's - 4219 Hollowfern Ln S, Keizer, 97418</div>

    <p class="details tagline">There will be dinner, games,<br>friends, and a message.</p>
  </main>
</body>
</html>
```